Fitness Body Weight Exercises Book Cover

Need a book cover design for a new book

This book is going to market to people to get in shape by playing a fitness dice game call FlexTRIO The dice game

When people see the cover they should see that this is a book that can help them get in shape. We are positioning the guru as an expert inside of the fitness niche

Target Market(s)

fitness

Requirements
Must have
• The name of the book which is

"The Grand Summit Frame Regimen"

Tagline -

The Worlds #1 Resource For Combat Strength Training Using Body Weight Exercises For Men, Women and Children

__________

Featuring FlexTRIO The Dice Game (TM)

___________________________
ON THE BACK COVER

Image with Oren with his gold medal
with these words
No Weights, No Problem

_____-

front cover
the image with him doing a push up should be on the front of the cover with these words

_________
Nice to have
• Maybe

"Oren Presents ...."

The Grand Summit Frame Regimen

```html
<!DOCTYPE html>
<html lang="en">
<head>
<meta charset="utf-8">
<title>The Grand Summit Frame Regimen — Book Cover</title>
<link rel="stylesheet" href="https://fonts.googleapis.com/css2?family=Archivo:wght@700;800;900&family=Oswald:wght@600;700&family=Roboto+Condensed:wght@700&display=swap">
<style>
  :root {
    --ink-black: #0b0d12;
    --slate: #1c2129;
    --slate-light: #3a4049;
    --navy: #1e2a3d;
    --sky: #5d7a99;
    --yellow: #f5e61c;
    --red: #e02424;
    --white: #ffffff;
    --frame: #2b3038;
    --skin: #8a5a3c;
  }
  * { margin: 0; padding: 0; box-sizing: border-box; }
  html, body { width: 1200px; height: 833px; overflow: hidden; background: var(--ink-black); }
  .cover-spread {
    position: relative; width: 1200px; height: 833px; overflow: hidden;
    font-family: "Archivo", Arial, sans-serif; color: var(--white);
  }

  /* Back cover */
  .back-cover {
    position: absolute; left: 0; top: 0; width: 566px; height: 833px;
    background: radial-gradient(ellipse at 45% 30%, #3b4048 0%, #23272e 45%, #15181d 100%);
  }
  .back-frame {
    position: absolute; left: 82px; top: 31px; width: 415px; height: 569px;
    background: linear-gradient(180deg, #3a3f47 0%, #2b2f36 100%);
    box-shadow: 0 0 18px rgba(0,0,0,.6);
  }
  .medal-photo {
    position: absolute; left: 29px; top: 20px; width: 357px; height: 386px;
    border: 1px solid #8d939b;
    background: radial-gradient(ellipse at 50% 55%, #7a5038 0%, #3a2a22 40%, #0e0f12 80%);
  }
  .back-slogan {
    position: absolute; left: 0; top: 466px; width: 100%;
    text-align: center; font-weight: 700; font-size: 33px; line-height: 48px;
    color: var(--white); text-shadow: 0 2px 4px rgba(0,0,0,.6);
  }

  /* Spine */
  .spine {
    position: absolute; left: 566px; top: 0; width: 58px; height: 833px;
    background: linear-gradient(90deg, #0f1216 0%, #1a1e25 50%, #0f1216 100%);
    display: flex; justify-content: center;
  }
  .spine-text {
    writing-mode: vertical-rl; height: 833px;
    display: flex; align-items: center; justify-content: space-between;
    padding: 24px 0 40px;
  }
  .spine-feature { font-size: 12px; font-weight: 700; color: var(--white); align-self: flex-end; margin-right: 4px; }
  .spine-title {
    font-family: "Oswald", "Arial Narrow", sans-serif; font-weight: 700;
    font-size: 25px; color: var(--yellow); letter-spacing: .3px;
  }
  .spine-presenter { font-size: 12px; font-weight: 700; color: var(--white); }

  /* Front cover */
  .front-cover {
    position: absolute; left: 624px; top: 0; width: 576px; height: 833px;
    background:
      radial-gradient(ellipse at 60% 5%, rgba(93,122,153,.85) 0%, rgba(40,56,80,.6) 30%, rgba(12,14,20,0) 60%),
      linear-gradient(180deg, #1d2a3c 0%, #10141b 45%, #0b0d12 100%);
  }
  .tagline {
    position: absolute; left: 20px; top: 60px; width: 540px;
    text-align: center; font-family: "Roboto Condensed", "Archivo", sans-serif;
    font-weight: 700; font-size: 33px; line-height: 38px;
    text-shadow: 0 2px 4px rgba(0,0,0,.7);
  }
  .tagline .rank { color: var(--red); font-size: 40px; }
  .tagline .highlight { color: var(--yellow); }
  .presenter {
    position: absolute; left: 58px; top: 256px;
    font-size: 21px; font-weight: 700; color: var(--white);
  }
  .pushup-photo {
    position: absolute; left: 53px; top: 309px; width: 480px; height: 274px;
    background:
      radial-gradient(ellipse at 50% 40%, #8a5a3c 0%, #5c3b28 30%, rgba(60,62,66,0) 60%),
      linear-gradient(180deg, #2a2d33 0%, #54575c 70%, #777a7f 100%);
    box-shadow: 0 0 24px rgba(0,0,0,.7);
  }
  .book-title {
    position: absolute; left: 0; top: 620px; width: 576px;
    text-align: center; font-family: "Oswald", "Arial Narrow", sans-serif;
    font-weight: 700; font-size: 50px; line-height: 58px;
    color: var(--yellow); text-transform: uppercase;
  }
  .feature-line {
    position: absolute; left: 0; top: 790px; width: 576px;
    text-align: center; font-size: 18px; font-weight: 700; color: var(--white);
  }
</style>
</head>
<body>
<main class="cover-spread">
  <section class="back-cover">
    <div class="back-frame">
      <div class="medal-photo" role="img" aria-label="Photo of Oren smiling, shirtless, wearing his gold medal"></div>
      <p class="back-slogan">No Weights,<br>No Problem</p>
    </div>
  </section>

  <section class="spine">
    <div class="spine-text">
      <span class="spine-presenter">Oren Presents ....</span>
      <span class="spine-title">THE GRAND SUMMIT FRAME REGIMEN</span>
      <span class="spine-feature">Featuring FlexTRIO The Dice Game (TM)</span>
    </div>
  </section>

  <section class="front-cover">
    <h2 class="tagline">
      The Worlds <span class="rank">#1</span> Resource<br>
      For Combat Strength Training<br>
      <span class="highlight">Using Body Weight</span> Exercises<br>
      For Men, Women and Children
    </h2>
    <p class="presenter">Oren Presents ....</p>
    <div class="pushup-photo" role="img" aria-label="Photo of Oren doing a push-up outdoors"></div>
    <h1 class="book-title">The Grand Summit<br>Frame Regimen</h1>
    <p class="feature-line">Featuring FlexTRIO The Dice Game (TM)</p>
  </section>
</main>
</body>
</html>
```